College Admissions Consulting needs a small street facing sign for new office location.

I need a graphic design to be used inside window for a banner/sign in office location on a high walking traffic city street, for my company, Campus Lantern. I work with high school students and families on the college planning and selection application process. Please check out the website to learn more about what I do (www.mycampuslantern.example). The banner will be used to market our services at our office location. The final design should utilize logo colors, phone number, and website/email information. I'd like to incorporate a my picture in someway because of face recognition. To be printed on a posterboard or vinyl banner.

Target Market(s)

Parents of high school aged children.

Industry/Entity Type

Education

Font styles to use
Sans Serif

Colors
abd037

Requirements
Must have
• Clean, attractive, and professional design. Attract the attention of people walking by. Information must be clear and readable (phone/email, etc.).
Nice to have
• Utilize the picture with crossed arms (without the brown background on picture).
Emphasize tagline:
Mastering The College Admission Process
....with personalized, professional guidance in planning, selecting, and applying to the right colleges.

```html
<!DOCTYPE html>
<html lang="en">
<head>
<meta charset="utf-8">
<title>Campus Lantern – 4x2 Window Banner</title>
<link rel="stylesheet" href="https://fonts.googleapis.com/css2?family=Oswald:wght@300&family=Playfair+Display:wght@700&display=swap">
<style>
  :root{
    --lime:#abd037;
    --lime-deep:#a2c532;
    --ink:#1a1a1a;
    --board:#363636;
    --paper:#ffffff;
    --mist:#e8e8e8;
    --slate:#555555;
    --serif:"Playfair Display", Georgia, serif;
    --condensed:"Oswald", "Arial Narrow", sans-serif;
  }
  *{margin:0;padding:0;box-sizing:border-box}
  html,body{width:1077px;height:1200px;overflow:hidden;background:var(--board)}
  .sheet{position:relative;width:1077px;height:1200px}
  .sheet-title{
    position:absolute;top:55px;left:0;width:100%;text-align:center;
    font-family:var(--condensed);font-weight:300;font-size:42px;
    letter-spacing:.42em;color:var(--paper);padding-left:.42em;
  }
  .sample-label{
    position:absolute;left:1030px;width:0;height:0;
    font-family:var(--condensed);font-weight:300;font-size:30px;
    letter-spacing:.3em;color:var(--paper);white-space:nowrap;
  }
  .sample-label span{display:block;transform:translate(-50%,-50%) rotate(-90deg);transform-origin:center;position:absolute;left:0;top:0;}
  .sample-label.one{top:518px}
  .sample-label.two{top:1027px}

  .banner{position:absolute;left:88px;width:909px;height:457px;overflow:hidden;font-family:var(--serif);font-weight:700}
  .banner.one{top:147px}
  .banner.two{top:665px;height:454px}
  .backdrop{position:absolute;inset:0;width:100%;height:100%}

  .portrait{
    position:absolute;left:690px;top:0;width:200px;height:373px;
    border-radius:95px 95px 0 0;
    background:linear-gradient(180deg,#2d2420 0%,#3a2c25 22%,#c9a18c 36%,#b98f7a 46%,#1f1c1b 58%,#141414 100%);
  }

  .headline{position:absolute;left:30px;top:14px;color:var(--paper);font-size:58px;line-height:59px;letter-spacing:-.01em}
  .tagline{position:absolute;left:32px;top:146px;width:500px;color:var(--ink);font-size:22px;line-height:28.5px}
  .banner.two .tagline{top:150px;width:520px;font-size:23px;line-height:30px}
  .banner.two .headline{top:18px;font-size:57px;line-height:59px}

  .brand{position:absolute;left:28px;top:271px;display:flex;align-items:center;gap:12px}
  .brand-dot{width:36px;height:36px;border-radius:50%;background:var(--lime)}
  .brand-name{font-size:36px;color:var(--slate);line-height:1}
  .banner.two .brand{top:260px}

  .offer{position:absolute;left:30px;top:344px;font-size:29px;letter-spacing:.12em;color:var(--ink);line-height:36px}
  .banner.two .offer{top:336px}

  .contact-bar{position:absolute;left:0;top:381px;width:909px;height:76px;display:flex;align-items:center}
  .banner.two .contact-bar{height:73px}
  .phone-icon{margin-left:12px;width:42px;height:44px;flex:none}
  .phone-number{margin-left:11px;font-size:46px;color:var(--paper);line-height:1;white-space:nowrap}
  .divider{width:2px;height:50px;background:var(--lime);margin-left:18px;flex:none}
  .links{margin-left:16px;display:flex;flex-direction:column;gap:6px}
  .link{display:flex;align-items:center;gap:10px;color:var(--paper);font-size:18.5px;line-height:1;white-space:nowrap}
  .link svg{width:21px;height:21px;flex:none}
</style>
</head>
<body>
<main class="sheet">
  <h1 class="sheet-title">4X2 WINDOW BANNER</h1>

  <section class="banner one" aria-label="Window banner, sample 1">
    <svg class="backdrop" viewBox="0 0 909 457" preserveAspectRatio="none" aria-hidden="true">
      <rect width="909" height="457" fill="var(--lime)"/>
      <g fill="var(--lime-deep)" opacity=".8">
        <circle cx="140" cy="55" r="38"/>
        <circle cx="240" cy="80" r="30"/>
        <circle cx="590" cy="150" r="45"/>
        <circle cx="495" cy="225" r="22"/>
        <circle cx="610" cy="290" r="40"/>
        <circle cx="420" cy="250" r="35"/>
        <circle cx="15" cy="205" r="12"/>
        <circle cx="15" cy="27" r="8"/>
      </g>
      <path d="M0,252 C170,222 420,230 582,374 L0,374 Z" fill="var(--paper)"/>
      <circle cx="750" cy="240" r="168" fill="var(--mist)" stroke="var(--paper)" stroke-width="13"/>
      <path d="M0,344 L425,344 Q440,344 446,360 L452,374 L0,374 Z" fill="var(--lime)"/>
      <rect y="374" width="909" height="8" fill="var(--lime)"/>
      <rect y="381" width="909" height="76" fill="var(--ink)"/>
    </svg>
    <div class="portrait" role="img" aria-label="Photo of the consultant, smiling with arms crossed, in a black top"></div>

    <h2 class="headline">Mastering The College<br>Admission Process</h2>
    <p class="tagline">With Personalized, Professional Guidance in Planning, Selecting, and Applying to the Right Colleges.</p>
    <div class="brand"><span class="brand-dot"></span><span class="brand-name">Campus Lantern</span></div>
    <p class="offer">FREE CONSULTATION</p>

    <div class="contact-bar">
      <svg class="phone-icon" viewBox="0 0 42 44" aria-hidden="true">
        <rect x="14" y="2" width="22" height="40" rx="4" fill="var(--lime)"/>
        <rect x="18" y="8" width="14" height="26" fill="var(--ink)"/>
        <path d="M2,26 Q2,20 10,18 L16,18 L16,40 L6,40 Q2,38 2,32 Z" fill="var(--lime)"/>
      </svg>
      <span class="phone-number">555-014-PLAN (7526)</span>
      <span class="divider"></span>
      <div class="links">
        <span class="link">
          <svg viewBox="0 0 22 22" aria-hidden="true"><circle cx="11" cy="11" r="11" fill="var(--lime)"/><rect x="5" y="7" width="12" height="8" fill="none" stroke="var(--ink)" stroke-width="1.5"/><path d="M5,7 L11,12 L17,7" fill="none" stroke="var(--ink)" stroke-width="1.5"/></svg>
          nora@mycampuslantern.example
        </span>
        <span class="link">
          <svg viewBox="0 0 22 22" aria-hidden="true"><circle cx="11" cy="11" r="9.5" fill="none" stroke="var(--lime)" stroke-width="2"/><ellipse cx="11" cy="11" rx="4" ry="9.5" fill="none" stroke="var(--lime)" stroke-width="1.6"/><path d="M1.5,11 H20.5 M3,6.5 H19 M3,15.5 H19" stroke="var(--lime)" stroke-width="1.6"/></svg>
          www.mycampuslantern.example
        </span>
      </div>
    </div>
  </section>

  <section class="banner two" aria-label="Window banner, sample 2">
    <svg class="backdrop" viewBox="0 0 909 454" preserveAspectRatio="none" aria-hidden="true">
      <rect width="909" height="454" fill="var(--paper)"/>
      <rect width="909" height="149" fill="var(--ink)"/>
      <rect y="149" width="909" height="105" fill="var(--lime)"/>
      <circle cx="495" cy="233" r="22" fill="var(--lime-deep)"/>
      <circle cx="405" cy="302" r="42" fill="#f2f2f2"/>
      <circle cx="610" cy="302" r="42" fill="#f2f2f2"/>
      <circle cx="752" cy="250" r="172" fill="var(--paper)" stroke="var(--lime)" stroke-width="14"/>
      <path d="M0,343 L425,343 Q440,343 446,358 L452,373 L0,373 Z" fill="var(--lime)"/>
      <rect y="373" width="909" height="8" fill="var(--lime)"/>
      <rect y="381" width="909" height="73" fill="var(--ink)"/>
    </svg>
    <div class="portrait" role="img" aria-label="Photo of the consultant, smiling with arms crossed, in a black top"></div>

    <h2 class="headline">Mastering The College<br>Admission Process</h2>
    <p class="tagline">With Personalized, Professional Guidance in Planning, Selecting, and Applying to the Right Colleges.</p>
    <div class="brand"><span class="brand-dot"></span><span class="brand-name">Campus Lantern</span></div>
    <p class="offer">FREE CONSULTATION</p>

    <div class="contact-bar">
      <svg class="phone-icon" viewBox="0 0 42 44" aria-hidden="true">
        <rect x="14" y="2" width="22" height="40" rx="4" fill="var(--lime)"/>
        <rect x="18" y="8" width="14" height="26" fill="var(--ink)"/>
        <path d="M2,26 Q2,20 10,18 L16,18 L16,40 L6,40 Q2,38 2,32 Z" fill="var(--lime)"/>
      </svg>
      <span class="phone-number">555-014-PLAN (7526)</span>
      <span class="divider"></span>
      <div class="links">
        <span class="link">
          <svg viewBox="0 0 22 22" aria-hidden="true"><circle cx="11" cy="11" r="11" fill="var(--lime)"/><rect x="5" y="7" width="12" height="8" fill="none" stroke="var(--ink)" stroke-width="1.5"/><path d="M5,7 L11,12 L17,7" fill="none" stroke="var(--ink)" stroke-width="1.5"/></svg>
          nora@mycampuslantern.example
        </span>
        <span class="link">
          <svg viewBox="0 0 22 22" aria-hidden="true"><circle cx="11" cy="11" r="9.5" fill="none" stroke="var(--lime)" stroke-width="2"/><ellipse cx="11" cy="11" rx="4" ry="9.5" fill="none" stroke="var(--lime)" stroke-width="1.6"/><path d="M1.5,11 H20.5 M3,6.5 H19 M3,15.5 H19" stroke="var(--lime)" stroke-width="1.6"/></svg>
          www.mycampuslantern.example
        </span>
      </div>
    </div>
  </section>

  <p class="sample-label one"><span>SAMPLE 1</span></p>
  <p class="sample-label two"><span>SAMPLE 2</span></p>
</main>
</body>
</html>
```